Stonebay Towing Business Card

Towing
Accident towing
Mechanical breakdown
Insurance, salvage and recovery
4wd off road towing
Light & Heavy towing
8347 2516
24 hour business 7 days

Logo can be whole size on front

Industry/Entity Type

Towing/ transport

Contact Information for Business Card

The above

```html
<!DOCTYPE html>
<html lang="en">
<head>
<meta charset="UTF-8">
<title>Stonebay Towing – Business Card</title>
<link rel="stylesheet" href="https://fonts.googleapis.com/css2?family=Poppins:wght@500;600;700;800&display=swap">
<style>
  :root {
    --brand-red: #d9141d;
    --ink-black: #1a1718;
    --card-white: #f6f5f3;
    --stage: #6b6b6b;
    --text-light: #ffffff;
  }
  * { box-sizing: border-box; margin: 0; padding: 0; }
  html, body {
    width: 1200px; height: 900px; overflow: hidden;
    background: var(--stage);
    font-family: "Poppins", sans-serif;
  }
  .canvas { position: relative; width: 1200px; height: 900px; }

  .card {
    position: absolute; left: 250px; width: 700px; height: 400px;
    overflow: hidden; box-shadow: 0 10px 30px rgba(0,0,0,.3);
  }
  .card--front { top: 35px; background: var(--card-white); }
  .card--back { top: 465px; background: var(--brand-red); display: flex; align-items: center; justify-content: center; }

  .card__shapes { position: absolute; inset: 0; }

  .brand-name {
    position: absolute; left: 62px; top: 112px;
    font-weight: 800; font-size: 46px; line-height: 1.02;
    color: var(--brand-red); letter-spacing: -0.5px;
  }
  .brand-name--large {
    position: static; font-size: 78px; color: var(--text-light); text-align: center;
  }

  .phone {
    position: absolute; right: 34px; top: 44px;
    display: flex; align-items: center; gap: 10px;
    font-weight: 700; font-size: 40px; color: var(--ink-black); letter-spacing: 0.5px;
  }
  .phone__icon { width: 26px; height: 26px; }

  .badge { position: absolute; left: 518px; top: 98px; width: 148px; height: 148px; }

  .services {
    position: absolute; list-style: none;
    color: var(--text-light); font-weight: 500; font-size: 14px; text-transform: uppercase;
    letter-spacing: 0.3px;
  }
  .services--left { left: 222px; top: 318px; }
  .services--right { left: 420px; top: 254px; }
  .services li { position: relative; display: flex; align-items: center; gap: 9px; line-height: 25px; }
  .services li::before {
    content: ""; width: 13px; height: 13px; border-radius: 50%; flex: none;
    background: var(--brand-red);
  }
  .services li::after {
    content: ""; position: absolute; left: 4.5px; top: 8.5px;
    width: 3px; height: 6px; border: solid var(--text-light);
    border-width: 0 1.6px 1.6px 0; transform: rotate(45deg);
  }
</style>
</head>
<body>
<main class="canvas">

  <section class="card card--front" aria-label="Business card front">
    <svg class="card__shapes" viewBox="0 0 700 400" aria-hidden="true">
      <path d="M0,300 C150,250 380,200 700,185 L700,215 C420,225 230,270 150,400 L0,400 Z" fill="var(--brand-red)"/>
      <path d="M150,400 C230,270 420,225 700,215 L700,400 Z" fill="var(--ink-black)"/>
      <path d="M40,350 C120,292 230,258 330,243" fill="none" stroke="var(--text-light)" stroke-width="2.5" stroke-linecap="round"/>
    </svg>

    <h1 class="brand-name">Stonebay<br>Towing</h1>

    <div class="phone">
      <svg class="phone__icon" viewBox="0 0 24 24" aria-hidden="true">
        <path fill="var(--brand-red)" d="M6.6 10.8a15.1 15.1 0 0 0 6.6 6.6l2.2-2.2c.3-.3.7-.4 1-.2 1.1.4 2.3.6 3.6.6.6 0 1 .4 1 1V20c0 .6-.4 1-1 1C10.6 21 3 13.4 3 4c0-.6.4-1 1-1h3.5c.6 0 1 .4 1 1 0 1.3.2 2.5.6 3.6.1.3 0 .7-.2 1z"/>
      </svg>
      <span>8347 2516</span>
    </div>

    <svg class="badge" viewBox="0 0 148 148" role="img" aria-label="24 hour business, 7 days">
      <circle cx="74" cy="74" r="72" fill="var(--ink-black)"/>
      <circle cx="74" cy="74" r="63" fill="none" stroke="var(--text-light)" stroke-width="9" stroke-dasharray="1.6 6.65"/>
      <circle cx="74" cy="74" r="50" fill="var(--brand-red)"/>
      <text x="66" y="80" text-anchor="middle" font-family="Poppins, sans-serif" font-weight="800" font-size="42" fill="var(--text-light)">24</text>
      <text x="0" y="0" transform="translate(112 74) rotate(-90)" text-anchor="middle" font-family="Poppins, sans-serif" font-weight="600" font-size="11" fill="var(--text-light)">HOUR</text>
      <text x="72" y="96" text-anchor="middle" font-family="Poppins, sans-serif" font-weight="600" font-size="10.5" fill="var(--text-light)">BUSINESS</text>
      <text x="72" y="111" text-anchor="middle" font-family="Poppins, sans-serif" font-weight="600" font-size="13" fill="var(--text-light)">7 DAYS</text>
    </svg>

    <ul class="services services--left">
      <li>Towing</li>
      <li>Accident towing</li>
      <li>Mechanical breakdown</li>
    </ul>
    <ul class="services services--right">
      <li>Insurance, salvage &amp; recovery</li>
      <li>4WD off road towing</li>
      <li>Light &amp; heavy towing</li>
    </ul>
  </section>

  <section class="card card--back" aria-label="Business card back">
    <h2 class="brand-name brand-name--large">Stonebay<br>Towing</h2>
  </section>

</main>
</body>
</html>
```